Business Card For Kelmora Financial Consulting

Hi, I would like a business card designed. Bold, modern.
Please use the same design as the logo. I have also attached the website design to see the overall theme.
Wordmark Font
Color: Hex: #01AEF7

```html
<!DOCTYPE html>
<html lang="en">
<head>
<meta charset="utf-8">
<title>Kelmora Financial Consulting – Business Card</title>
<link rel="stylesheet" href="https://fonts.googleapis.com/css2?family=Poppins:wght@400;500;600;700&display=swap">
<style>
  :root {
    --brand-blue: #01aef7;
    --line-blue: #2a9ee0;
    --card-dark: #13202a;
    --panel-start: #3b5fb0;
    --panel-end: #2fbbea;
    --ink-dark: #101820;
    --white: #ffffff;
    --page-bg: #e9ecef;
  }
  * { box-sizing: border-box; margin: 0; padding: 0; }
  html, body {
    width: 1200px; height: 900px; overflow: hidden;
    background: var(--page-bg);
    font-family: "Poppins", sans-serif;
  }
  .sheet {
    position: relative; width: 1200px; height: 900px;
    display: flex; flex-direction: column; align-items: center; justify-content: center; gap: 36px;
  }
  .card {
    position: relative; width: 700px; height: 400px;
    background: var(--card-dark); overflow: hidden;
    box-shadow: 0 8px 24px rgba(0,0,0,0.18);
  }

  /* Brand lockup */
  .brand { display: flex; align-items: center; gap: 10px; }
  .brand-square {
    width: 38px; height: 38px; border: 3px solid var(--brand-blue);
  }
  .brand-name {
    color: var(--white); font-weight: 600; line-height: 1;
  }
  .brand-name .word { display: block; font-size: 30px; letter-spacing: 2px; }
  .brand-name .sub { display: block; font-size: 9px; letter-spacing: 12.4px; margin-top: 4px; }

  /* Logo side */
  .card--logo .band {
    position: absolute; top: 186px; height: 28px; background: var(--brand-blue);
  }
  .card--logo .band--left { left: 0; width: 205px; }
  .card--logo .band--right { right: 0; width: 205px; }
  .card--logo .brand {
    position: absolute; left: 50%; top: 50%; transform: translate(-50%, -50%);
  }

  /* Contact side */
  .card--contact .brand {
    position: absolute; left: 50%; top: 40px; transform: translateX(-50%);
  }
  .rule {
    position: absolute; left: 0; width: 100%; height: 3px; background: var(--line-blue);
  }
  .rule--top { top: 110px; }
  .rule--bottom { top: 304px; }
  .panel {
    position: absolute; left: 0; top: 120px; width: 100%; height: 176px;
    background: linear-gradient(90deg, var(--panel-start), var(--panel-end));
    text-align: center; color: var(--ink-dark);
  }
  .person-name {
    margin-top: 26px; color: var(--white); font-weight: 700; font-size: 24px; letter-spacing: 0.5px; line-height: 1.1;
  }
  .person-title { font-size: 16px; font-weight: 500; line-height: 1.2; }
  .contact-row {
    margin-top: 16px; display: flex; justify-content: center; gap: 24px;
    font-size: 13px; font-weight: 500;
  }
  .contact-row .value { color: var(--white); }
  .address { margin-top: 8px; font-size: 13px; font-weight: 600; }
  .website {
    position: absolute; left: 0; bottom: 34px; width: 100%; text-align: center;
    font-size: 20px; font-weight: 500; letter-spacing: 2px; color: var(--white);
  }
  .website .accent { color: var(--brand-blue); }
</style>
</head>
<body>
<main class="sheet">
  <section class="card card--logo" aria-label="Business card, brand side">
    <div class="band band--left"></div>
    <div class="band band--right"></div>
    <div class="brand">
      <div class="brand-square"></div>
      <div class="brand-name"><span class="word">KELMORA</span><span class="sub">CONSULTING</span></div>
    </div>
  </section>

  <section class="card card--contact" aria-label="Business card, contact side">
    <div class="brand">
      <div class="brand-square"></div>
      <div class="brand-name"><span class="word">KELMORA</span><span class="sub">CONSULTING</span></div>
    </div>
    <div class="rule rule--top"></div>
    <div class="panel">
      <h1 class="person-name">DANA M. HOLLIS</h1>
      <p class="person-title">President</p>
      <div class="contact-row">
        <span>Phone: <span class="value">555-201-4380</span></span>
        <span>Fax: <span class="value">555-201-4381</span></span>
        <span>Email: <span class="value">hello@kelmoraadvisors.com</span></span>
      </div>
      <p class="address">2250 Larkfield Avenue Ste 120, Brookhaven, OH 43999</p>
    </div>
    <div class="rule rule--bottom"></div>
    <p class="website"><span class="accent">www.</span>kelmoraconsulting<span class="accent">.com</span></p>
  </section>
</main>
</body>
</html>
```